Elegant sophisticated Invitation Design in A5

"Amber Hours of Vellmoor"
We are after an invitation A5 portrait size. It is for an outdoor event for a 4 course dinner. It needs to display high class, elegance and sophistication. We like the idea of having stars or reflections on the water (as per attached images we found on findora)

Text and logo are attached. The file needs to be supplied to use as psd file and needs to be 300dpi at least as the invitation will be printed.

We would like dark colours, black, and sparkles/stars.

The main focus is elegance!

Logos and text are attached.

Target Market(s)

Upper class, business men and women, Suit and tie event

Industry/Entity Type

Event

Font styles to use
Decorative
Script

Colors
fffefe
000000

Requirements
Must have
• The element of Water and stars or sparkles. It needs to speak elegance throughout. The fonts chosen need to be soft and elegant. The logo attached must be used either with the diamond or the standard version a mono version can also be used. Open for designers ideas.
Should not have
• Bold and bulky fonts it needs to be soft

```html
<!DOCTYPE html>
<html lang="en">
<head>
<meta charset="utf-8">
<title>Amber Hours of Vellmoor – VIP Dinner Invitation</title>
<link href="https://fonts.googleapis.com/css2?family=Pinyon+Script&family=Cormorant+Garamond:wght@500&family=Montserrat:ital,wght@0,300;0,400;0,600;1,600&display=swap" rel="stylesheet">
<style>
  :root {
    --backdrop: #d9d9d9;
    --ink: #000000;
    --paper-text: #fffefe;
    --soft-text: #ece9e4;
    --amber-deep: #2e1606;
    --amber-mid: #7a4a14;
    --amber-light: #d8b65a;
    --glow: rgba(255, 236, 170, 0.55);
    --glow-warm: rgba(255, 190, 110, 0.4);
  }
  * { margin: 0; padding: 0; box-sizing: border-box; }
  html, body {
    width: 1200px;
    height: 960px;
    overflow: hidden;
    background: var(--backdrop);
  }
  .invitation {
    position: absolute;
    left: 296px;
    top: 50px;
    width: 608px;
    height: 860px;
    background: var(--ink);
    color: var(--paper-text);
    font-family: "Montserrat", sans-serif;
    overflow: hidden;
  }
  .water-reflection {
    position: absolute;
    left: 0;
    right: 0;
    top: 510px;
    bottom: 0;
    background:
      radial-gradient(ellipse 60% 30% at 25% 70%, var(--glow), transparent 70%),
      radial-gradient(ellipse 55% 28% at 75% 55%, var(--glow-warm), transparent 70%),
      radial-gradient(ellipse 70% 25% at 50% 95%, var(--glow), transparent 70%),
      linear-gradient(to bottom,
        rgba(0,0,0,0) 0%,
        var(--amber-deep) 22%,
        var(--amber-mid) 60%,
        var(--amber-light) 100%);
  }
  .line {
    position: absolute;
    left: 0;
    width: 100%;
    text-align: center;
    white-space: nowrap;
  }
  .brand {
    top: 76px;
    display: flex;
    justify-content: center;
    align-items: center;
    gap: 8px;
    font-size: 15px;
    line-height: 18px;
    font-weight: 400;
  }
  .brand-dot {
    width: 12px;
    height: 12px;
    border-radius: 50%;
    background: var(--paper-text);
  }
  .presenter { top: 133px; font-size: 14px; line-height: 17px; font-weight: 400; }
  .event-title {
    top: 178px;
    font-family: "Pinyon Script", cursive;
    font-weight: 400;
    font-size: 50px;
    line-height: 60px;
  }
  .event-kind { top: 250px; font-size: 16px; line-height: 19px; font-weight: 400; }
  .event-name {
    top: 266px;
    font-family: "Cormorant Garamond", serif;
    font-weight: 500;
    font-size: 37px;
    line-height: 42px;
    letter-spacing: 0.5px;
  }
  .event-date { top: 329px; font-size: 14.5px; line-height: 17px; font-weight: 300; }
  .venue-name { top: 362px; font-size: 14.5px; line-height: 18px; font-weight: 600; }
  .venue-address { top: 380px; font-size: 14.5px; line-height: 18px; font-weight: 300; }
  .cause { top: 411px; font-size: 10.5px; line-height: 13px; font-weight: 600; font-style: italic; }
  .admission { top: 439px; font-size: 15px; line-height: 18px; font-weight: 600; }
  .inclusions {
    position: absolute;
    top: 470px;
    left: 0;
    width: 100%;
    list-style: none;
    text-align: center;
    font-size: 9.5px;
    font-weight: 400;
    line-height: 15px;
    color: var(--soft-text);
  }
  .inclusions li::before {
    content: "";
    display: inline-block;
    width: 4px;
    height: 4px;
    border-radius: 50%;
    background: var(--paper-text);
    margin-right: 8px;
    vertical-align: 2px;
  }
</style>
</head>
<body>
  <article class="invitation">
    <div class="water-reflection" role="img" aria-label="Golden bokeh lights and star sparkles reflecting on night water"></div>

    <div class="line brand"><span class="brand-dot"></span><span>Marlowe Coast Care</span></div>

    <p class="line presenter">MARLOWE COAST CARE’S INAUGURAL</p>
    <h1 class="line event-title">Amber Hours of Vellmoor</h1>
    <p class="line event-kind">VIP DINNER</p>
    <h2 class="line event-name">LE BANQUET</h2>
    <p class="line event-date">SATURDAY 17TH JULY 2017</p>
    <p class="line venue-name">HARBOURLIGHT GARDENS</p>
    <p class="line venue-address">QUAYLINE ROAD, VELLMOOR SOUTH</p>
    <p class="line cause">BUILDING ACCESSIBLE HOUSING FOR PEOPLE WITH DISABILITY ON THE NORTHERN COAST</p>
    <p class="line admission">BY INVITATION</p>
    <ul class="inclusions">
      <li>FOUR COURSE DINNER EXCLUSIVELY CRAFTED BY SALTMERE KITCHEN</li>
      <li>BEAUTIFUL WINES AND FINE BEERS INCLUDED</li>
      <li>LIVE ENTERTAINMENT</li>
    </ul>
  </article>
</body>
</html>
```